Business Intelligence/Analytics Technology Company Business Card

We are a higher-end enterprise software development company working with Retailer POS data to provide business intelligence and analytical services to fortune 500 companies.

I have an immediate need for a professional/thick/bold business card. The same design aspects will spiral into more media such as flyers/folders/etc...

Our website is www.brenvolq.com for our product.

I like "Clean" designs if that makes sense, not a lot of "stuff".

The uploaded files, the A logo with the box is the style we're leaning towards, but the A logo without the blue box is all good too... get creative.

Target Market(s)

Executives of large companies, down to VP level..

Industry/Entity Type

Software

Requirements
Must have
• I'm wanting a thick designer like business card.

I think we're going to change our logo to a more quillmesh 8 looking style... http://www.brenvolq.com/card.ai as an example of our current business card.

The winner will also have knowledge of where i can get these things printed.
Nice to have
• Blue-ish color scheme? I'm open to anything. Our Competition is Red, and another is Green. So we'll stick with the Blue.

```html
<!DOCTYPE html>
<html lang="en">
<head>
<meta charset="utf-8">
<title>Brenvolq Business Card</title>
<link rel="stylesheet" href="https://fonts.googleapis.com/css2?family=Montserrat:wght@400;500;600&display=swap">
<style>
  :root {
    --bg: #e6e8eb;
    --blue-deep: #0b3f9a;
    --blue-mid: #1a5bc4;
    --blue-light: #3f7fd8;
    --white: #ffffff;
    --paper: #eef0f3;
    --grey-text: #6b6e73;
    --muted-blue: #7f9fd1;
    --accent: #a9c2ea;
  }
  * { margin: 0; padding: 0; box-sizing: border-box; }
  html, body { width: 1067px; height: 1200px; overflow: hidden; }
  body {
    background: var(--bg);
    font-family: "Montserrat", sans-serif;
    position: relative;
  }
  .card {
    position: absolute;
    left: 184px;
    width: 700px;
    height: 400px;
    border-radius: 4px;
    overflow: hidden;
    box-shadow: 0 10px 28px rgba(20, 40, 80, 0.22);
  }

  /* Front */
  .card-front {
    top: 110px;
    background: linear-gradient(135deg, var(--blue-light) 0%, var(--blue-mid) 45%, var(--blue-deep) 100%);
  }
  .front-glow {
    position: absolute;
    inset: 0;
    background: radial-gradient(ellipse at 30% 40%, rgba(255,255,255,0.14), rgba(255,255,255,0) 60%);
  }
  .front-brand {
    position: absolute;
    left: 0; right: 0; top: 118px;
    display: flex; flex-direction: column; align-items: center;
  }
  .brand-square {
    width: 112px; height: 100px;
    background: var(--white);
    margin-bottom: 22px;
  }
  .front-name {
    color: var(--white);
    font-weight: 600;
    font-size: 56px;
    letter-spacing: 5px;
    line-height: 1;
  }
  .front-url {
    margin-top: 22px;
    color: var(--muted-blue);
    font-size: 13px;
    letter-spacing: 1.5px;
    text-transform: uppercase;
  }

  /* Back */
  .card-back {
    top: 680px;
    background: linear-gradient(120deg, var(--white) 0%, var(--paper) 60%, #dde2ea 100%);
  }
  .back-brand {
    position: absolute;
    left: 40px; top: 34px;
    display: flex; align-items: center;
  }
  .back-square {
    width: 100px; height: 100px;
    background: var(--blue-mid);
    margin-right: 20px;
  }
  .back-name {
    color: var(--grey-text);
    font-weight: 600;
    font-size: 46px;
    letter-spacing: 4px;
    line-height: 1;
  }
  .back-tagline {
    color: var(--blue-mid);
    font-size: 13px;
    letter-spacing: 1.5px;
    margin-top: 8px;
  }
  .contact-band {
    position: absolute;
    left: 0; right: 0; bottom: 0;
    height: 218px;
    background: linear-gradient(120deg, var(--blue-mid) 0%, var(--blue-deep) 100%);
  }
  .contact-band::before {
    content: "";
    position: absolute;
    left: 40px; top: -14px;
    border-left: 16px solid transparent;
    border-right: 16px solid transparent;
    border-bottom: 14px solid var(--blue-mid);
  }
  .person {
    position: absolute;
    left: 40px; top: 52px;
    color: var(--white);
  }
  .person-name {
    font-weight: 600;
    font-size: 19px;
    letter-spacing: 0.5px;
    text-transform: uppercase;
  }
  .person-title {
    font-size: 12px;
    letter-spacing: 1px;
    margin-top: 6px;
    text-transform: uppercase;
    color: var(--accent);
  }
  .contact-lines { margin-top: 28px; font-size: 13px; letter-spacing: 0.8px; line-height: 1.55; }
  .contact-lines .label { color: var(--accent); font-weight: 600; }
  .divider {
    position: absolute;
    left: 352px; top: 30px;
    width: 1px; height: 158px;
    background: rgba(255,255,255,0.45);
  }
  .company {
    position: absolute;
    left: 376px; top: 30px;
    width: 290px;
    color: var(--white);
    font-size: 13px;
    letter-spacing: 0.6px;
    line-height: 1.45;
    text-transform: uppercase;
    white-space: nowrap;
  }
  .company .contact-lines { margin-top: 26px; }
</style>
</head>
<body>
  <section class="card card-front">
    <div class="front-glow"></div>
    <div class="front-brand">
      <div class="brand-square"></div>
      <div class="front-name">BRENVOLQ</div>
      <div class="front-url">www.brenvolq.com</div>
    </div>
  </section>

  <section class="card card-back">
    <div class="back-brand">
      <div class="back-square"></div>
      <div>
        <div class="back-name">BRENVOLQ</div>
        <div class="back-tagline">BRENVOLQ . SIGNAL . SHELF PULSE</div>
      </div>
    </div>
    <div class="contact-band">
      <div class="person">
        <div class="person-name">Dorian Kellaway</div>
        <div class="person-title">Business Director</div>
        <div class="contact-lines">
          <div><span class="label">E:</span> DORIAN@BRENVOLQ.COM</div>
          <div><span class="label">C:</span> 555.014.8820</div>
        </div>
      </div>
      <div class="divider"></div>
      <div class="company">
        <div>Brenvolq Technology Group, Inc</div>
        <div>1460 Harlow Ave, Suite 118</div>
        <div>Fenwick, AR 70014</div>
        <div class="contact-lines">
          <div><span class="label">P:</span> 555.014.3177</div>
          <div><span class="label">F:</span> 555.014.9046</div>
        </div>
      </div>
    </div>
  </section>
</body>
</html>
```